Freelance Makeup Artist Needing Business Card Design

I am a freelance makeup artist looking for a design for my business cards.
My target audience is people looking for bridal makeup, so i was thinking minimalistic style, black with white or gold foil accents.
Something that feels classy but simple and to the point.

I would like the front to state Naomi Carrow and Makeup Artist, and the back to include my social media and contact details.

Target Market(s)

Brides, young women

Industry/Entity Type

Business

Contact Information for Business Card

0417293846
naomi.carrow@mailvista.com
www.snapgrid.com/naomi.carrow
www.friendpage.com/NaomiCarrowMakeup

Requirements
Nice to have
• Social media icons next to relevant contact details

```html
<!DOCTYPE html>
<html lang="en">
<head>
<meta charset="utf-8">
<title>Naomi Carrow – Makeup Artist Business Card</title>
<link rel="stylesheet" href="https://fonts.googleapis.com/css2?family=Montserrat:wght@300;400&display=swap">
<style>
  :root {
    --backdrop: #a9aaab;
    --ink-black: #000000;
    --text-white: #ffffff;
    --text-grey: #b9b9b9;
    --rule-grey: #555555;
    --silver-dark: #8e8f91;
    --silver-mid: #c4c5c7;
    --silver-light: #f3f4f5;
    --silver-edge: #a3a4a6;
  }
  html, body {
    margin: 0;
    padding: 0;
    width: 1200px;
    height: 1000px;
    overflow: hidden;
    background: var(--backdrop);
    font-family: "Montserrat", sans-serif;
  }
  .canvas {
    position: relative;
    width: 1200px;
    height: 1000px;
  }
  .card {
    position: absolute;
    left: 302px;
    width: 595px;
    height: 347px;
    background: linear-gradient(90deg, var(--silver-dark) 0%, var(--silver-mid) 35%, var(--silver-light) 65%, var(--silver-mid) 82%, var(--silver-edge) 100%);
    overflow: hidden;
  }
  .card--front { top: 125px; }
  .card--back { top: 520px; height: 348px; }

  .front-panel {
    position: absolute;
    left: 44px;
    top: 40px;
    width: 509px;
    height: 267px;
    background: var(--ink-black);
    color: var(--text-white);
    text-align: center;
  }
  .brand-mark {
    position: absolute;
    left: 0;
    right: 0;
    font-weight: 300;
    letter-spacing: 0.12em;
    text-transform: uppercase;
  }
  .front-panel .brand-mark {
    top: 60px;
    font-size: 15px;
    color: var(--text-white);
  }
  .card-name {
    position: absolute;
    left: 0;
    right: 0;
    top: 142px;
    margin: 0;
    font-size: 29px;
    font-weight: 400;
    letter-spacing: 0.09em;
    text-transform: uppercase;
  }
  .card-rule {
    position: absolute;
    left: 62px;
    width: 384px;
    top: 189px;
    height: 1px;
    background: var(--rule-grey);
  }
  .card-title {
    position: absolute;
    left: 0;
    right: 0;
    top: 199px;
    margin: 0;
    font-size: 19px;
    font-weight: 300;
    letter-spacing: 0.22em;
    color: var(--text-grey);
    text-transform: uppercase;
    word-spacing: 0.4em;
  }

  .back-top {
    position: absolute;
    left: 0;
    top: 0;
    width: 100%;
    height: 192px;
  }
  .back-top .brand-mark {
    top: 86px;
    font-size: 15px;
    color: var(--ink-black);
    text-align: center;
  }
  .back-panel {
    position: absolute;
    left: 0;
    top: 192px;
    width: 100%;
    height: 156px;
    background: var(--ink-black);
  }
  .contact-list {
    list-style: none;
    margin: 0;
    padding: 0;
    position: absolute;
    left: 0;
    right: 0;
    top: 42px;
    text-align: center;
    color: var(--text-white);
    font-size: 13px;
    font-weight: 400;
    line-height: 17px;
  }
</style>
</head>
<body>
  <main class="canvas">
    <section class="card card--front" aria-label="Business card front">
      <div class="front-panel">
        <div class="brand-mark">Naomi Carrow</div>
        <h1 class="card-name">Naomi Carrow</h1>
        <div class="card-rule"></div>
        <p class="card-title">Makeup Artist</p>
      </div>
    </section>

    <section class="card card--back" aria-label="Business card back">
      <div class="back-top">
        <div class="brand-mark">Naomi Carrow</div>
      </div>
      <div class="back-panel">
        <ul class="contact-list">
          <li>0417293846</li>
          <li>naomi.carrow@mailvista.com</li>
          <li>www.snapgrid.com/naomi.carrow</li>
          <li>www.friendpage.com/NaomiCarrowMakeup</li>
        </ul>
      </div>
    </section>
  </main>
</body>
</html>
```